Corporate Identity – create a business card design to win

Dear Freelancers,

The competition is to create a complete set of Corporate Identity based on the logo I will give you. I will judge the winner based on the draft of a business card (front & back). You have to submit a business card design based on the given logo.

If you win the competition you will have to create the following additional items (based on the business card look and feel) included in the price of the competition. The winning price is for creating all items not just the business card. I need the business card to select the winner so he/ she can show design competency and to minimize the effort for the freelancer for the competition.

If you like you can use a template and incorporate your design. In this case I can pay for the template of your choice additionally. The winner will get the logo in the following version (ai,cdr)
I need at least the following:
1. (9.5×5.7cm) Businesscard (Front & Back), (Dark & Light)
2. DIN A4 Letterhead, (Dark & Light)
3. DIN A4 Invoice, (Dark & Light)
4. PowerPoint Presentation Template (16:9, 4:3), (Dark & Light). Template is based on Slide Master layouts, color set with section breaks, navigation buttons and placeholders for images and video. Ready to used.
5. DIN A5 Corporate Flyer(Front & Back), (Dark & Light)
6. DIN A5 Compliment Card (Front & Back)
7. DIN C5 Envelope
8. DVD – DVD Envelopes (Cd: 12×12 cm – Cd Envelope 37×12.5cm)
9. Presentation Folder with Bleed and Die-Cutting shape
10. Staff ID Card (10×6.3cm)
11. Facebook Timeline Cover (Dark & Light)
12. Wallpaper (Dark & Light)

The finals must be:
• Need the files in: PPT and PPTX as well as DOC and DOCX since I don’t have a graphic program to work with
• ALL TEMPLATE READY TO PRINT
• 300 DPI CMYK
• EASY EDITABLE LAYERED DESIGN
• LAYER DOESN'T LOSE QUALITY ( IF YOU CHANGE ITEM SIZE)
• ALL LAYER ARE VECTOR SHAPES
• CLEAN DESIGN
• USE GOOGLE FONTS
• CLEAN & CLEAR ELEGANT STYLE

Regards Kel

P.S. Details for mock-up business card:
Text for the front:
<logo>
Tactical Outreach Readiness Blueprint (TORB)
name: Marcus T. Hallvard
title: 7qu2Vmb
phone: +41 76 482 5730
mail: 7qu2Vmb@trovanmetric.com
web: torb.trovanmetric.com

Text for the back:
“The elicitation of information from systems, networks or human beings through methods and tools”

```html
<!DOCTYPE html>
<html lang="en">
<head>
<meta charset="utf-8">
<title>TORB Business Card – Front &amp; Back</title>
<link rel="stylesheet" href="https://fonts.googleapis.com/css2?family=Ubuntu:wght@400;500;700&family=Arimo:wght@400;700&family=Tinos:ital@1&display=swap">
<style>
  :root {
    --backdrop: #e8e5e0;
    --card: #272a31;
    --card-edge: #1d2026;
    --accent: #3eaee3;
    --white: #ffffff;
    --silver: #c9ccd1;
    --silver-dark: #8e9299;
    --ink: #23262c;
  }
  * { margin: 0; padding: 0; box-sizing: border-box; }
  html, body {
    width: 1200px;
    height: 852px;
    overflow: hidden;
    background: var(--backdrop);
  }
  .canvas {
    position: relative;
    width: 1200px;
    height: 852px;
  }
  .card {
    position: absolute;
    width: 525px;
    height: 315px;
    background: var(--card);
    border-radius: 16px;
    overflow: hidden;
    box-shadow: 0 6px 18px rgba(0, 0, 0, 0.25);
  }
  .card--front { left: 160px; top: 100px; }
  .card--back { left: 540px; top: 420px; }

  /* Front */
  .brand {
    position: absolute;
    left: 24px;
    top: 40px;
    display: flex;
    align-items: center;
    gap: 10px;
  }
  .brand__mark {
    width: 22px;
    height: 22px;
    background: var(--accent);
  }
  .brand__name {
    font-family: "Arimo", Arial, sans-serif;
    font-weight: 700;
    font-size: 28px;
    letter-spacing: 3px;
    color: var(--white);
  }
  .nameplate {
    position: absolute;
    left: 250px;
    top: 97px;
    width: 275px;
    height: 100px;
    background: var(--accent);
    padding: 18px 14px 0 0;
    text-align: right;
    box-shadow: -3px 3px 6px rgba(0, 0, 0, 0.35);
  }
  .nameplate__name {
    font-family: "Ubuntu", sans-serif;
    font-weight: 700;
    font-size: 29px;
    color: var(--white);
    line-height: 1.1;
  }
  .nameplate__title {
    font-family: "Ubuntu", sans-serif;
    font-weight: 400;
    font-size: 22px;
    letter-spacing: 2px;
    color: var(--white);
    margin-top: 8px;
  }
  .contact {
    position: absolute;
    left: 126px;
    top: 214px;
    list-style: none;
  }
  .contact__item {
    display: flex;
    align-items: center;
    gap: 12px;
    height: 24px;
    font-family: "Arimo", Arial, sans-serif;
    font-size: 19px;
    color: var(--white);
  }
  .contact__icon {
    width: 16px;
    height: 16px;
    flex: none;
  }

  /* Back */
  .quote {
    position: absolute;
    left: 17px;
    top: 120px;
    width: 257px;
    height: 106px;
    background: var(--accent);
    display: flex;
    align-items: center;
    justify-content: center;
    padding: 0 14px;
    box-shadow: 0 3px 6px rgba(0, 0, 0, 0.35);
  }
  .quote__text {
    font-family: "Tinos", "Times New Roman", serif;
    font-style: italic;
    font-size: 16px;
    line-height: 1.2;
    text-align: center;
    color: var(--white);
  }
  .emblem {
    position: absolute;
    left: 330px;
    top: 20px;
    width: 275px;
    height: 275px;
    border-radius: 50%;
    background: radial-gradient(circle at 35% 30%, var(--white), var(--silver) 45%, var(--silver-dark));
  }
  .emblem__name {
    position: absolute;
    left: 370px;
    top: 130px;
    font-family: "Arimo", Arial, sans-serif;
    font-weight: 700;
    font-size: 46px;
    letter-spacing: 8px;
    color: var(--ink);
  }
</style>
</head>
<body>
<main class="canvas">
  <section class="card card--front" aria-label="Business card front">
    <div class="brand">
      <span class="brand__mark"></span>
      <span class="brand__name">TORB</span>
    </div>
    <div class="nameplate">
      <div class="nameplate__name">Marcus T. Hallvard</div>
      <div class="nameplate__title">Position</div>
    </div>
    <ul class="contact">
      <li class="contact__item">
        <svg class="contact__icon" viewBox="0 0 16 16" aria-hidden="true">
          <path d="M4 1.5 L6.5 4.5 L5 6 C6 8 8 10 10 11 L11.5 9.5 L14.5 12 L12.5 14.5 C7 14 2 9 1.5 3.5 Z" fill="var(--white)"/>
        </svg>
        +41 76 482 5730
      </li>
      <li class="contact__item">
        <svg class="contact__icon" viewBox="0 0 16 16" aria-hidden="true">
          <rect x="1" y="3.5" width="14" height="10" rx="1" fill="var(--white)"/>
          <path d="M1.5 4 L8 9 L14.5 4" fill="none" stroke="var(--card)" stroke-width="1.3"/>
        </svg>
        7qu2Vmb@trovanmetric.com
      </li>
      <li class="contact__item">
        <svg class="contact__icon" viewBox="0 0 16 16" aria-hidden="true">
          <circle cx="8" cy="8" r="7" fill="var(--white)"/>
          <path d="M1 8 H15 M8 1 C5 4 5 12 8 15 M8 1 C11 4 11 12 8 15" fill="none" stroke="var(--card)" stroke-width="1.1"/>
        </svg>
        torb.trovanmetric.com
      </li>
    </ul>
  </section>

  <section class="card card--back" aria-label="Business card back">
    <div class="quote">
      <p class="quote__text">“The elicitation of information from systems, networks or human beings through methods and tools”</p>
    </div>
    <div class="emblem"></div>
    <span class="emblem__name">TORB</span>
  </section>
</main>
</body>
</html>
```